Word Page Templates x 5

1 x Letterhead Template with Header and Footer able to be printed to paper and pdf with non blurry resolution
- File attached looks ok on computer screen but does not print the same
- We are wanting it to print like it looks on the screen
- We are wanting it to print not fuzzy in resolution
- We are wanting the banner to be on the absolute edge of the page like it is on the computer screen
- We are needing to print this to paper and pdf with perfect resolution and colour

Please can someone help us!!

I have provided the logo files in our posession. If better resolutions are required please let us know.

We are also wanting 4 simple page templates to be setup in Landscape and Portrait orientation as well once we are happy with the letterhead that is provided samples have been provided
Updates

Hi all I have the vector files available now along with a Colour profile

Requirements
Must have
• Clear when printed on A4 Paper
Should not have
• Blurry images, Colour must be correct (same as Logo) - Please reference our website if need be ..... vornal.com.au

```html
<!DOCTYPE html>
<html lang="en">
<head>
<meta charset="utf-8">
<title>Vornal Pavement Services – Letterhead</title>
<link rel="stylesheet" href="https://fonts.googleapis.com/css2?family=Mulish:wght@800;900&display=swap">
<style>
  :root {
    --backdrop: #ece9e4;
    --paper: #ffffff;
    --brand-green: #0a7a3e;
    --brand-blue: #22398a;
    --ink-dark: #2b2b2b;
  }
  html, body {
    margin: 0;
    padding: 0;
    width: 1200px;
    height: 1000px;
    overflow: hidden;
    background: var(--backdrop);
  }
  .letterhead {
    position: absolute;
    left: 264px;
    top: 30px;
    width: 672px;
    height: 940px;
    background: var(--paper);
    box-shadow: 0 2px 10px rgba(0, 0, 0, 0.12);
    font-family: "Mulish", sans-serif;
  }
  .header-rule {
    position: absolute;
    left: 0;
    top: 19px;
    width: 240px;
    height: 20px;
    background: var(--brand-green);
  }
  .footer-rule {
    position: absolute;
    left: 0;
    top: 870px;
    width: 400px;
    height: 21px;
    background: var(--brand-green);
  }
  .company-mark {
    position: absolute;
    right: 22px;
    top: 864px;
    text-align: right;
  }
  .company-name {
    display: block;
    font-weight: 900;
    font-size: 40px;
    line-height: 40px;
    letter-spacing: 0.5px;
    color: var(--brand-blue);
  }
  .company-tagline {
    display: block;
    margin-top: 4px;
    font-weight: 800;
    font-size: 11px;
    line-height: 12px;
    letter-spacing: 0.4px;
    color: var(--ink-dark);
  }
</style>
</head>
<body>
  <main class="letterhead">
    <div class="header-rule" aria-hidden="true"></div>
    <div class="footer-rule" aria-hidden="true"></div>
    <div class="company-mark">
      <span class="company-name">VORNAL</span>
      <span class="company-tagline">PAVEMENT SERVICES</span>
    </div>
  </main>
</body>
</html>
```